Brisk Nibbles natural dog treats

We need a packaging design for a new brand of natural dog treats named Brisk Nibbles. Need the color scheme and template for the line of products that will be on flexible pouches or stand upright gusseted pouches.

Target Market(s)

Mass appeal with the majority being female. This will be a grocery store brand moderate price.

Industry/Entity Type

Grocery Store

Font styles to use
Serif
Sans Serif

Requirements
Must have
• Clean bright colors preferably yellow light blue etc. Very clean, memorable and simple packaging. This being a natural product it should also show natural with the packaging.
Nice to have
• Dog 30-50% of the packaging to be clear to show the product.
Should not have
• Not busy
Too much information on the front.

```html
<!DOCTYPE html>
<html lang="en">
<head>
<meta charset="UTF-8">
<title>Brisk Nibbles – Beef Sticks Pouch</title>
<link href="https://fonts.googleapis.com/css2?family=Oswald:wght@500;600;700&family=Luckiest+Guy&display=swap" rel="stylesheet">
<style>
  :root {
    --page-bg: #f4f2ee;
    --kraft: #c59c66;
    --kraft-dark: #b88c56;
    --purple: #3f1c5e;
    --navy: #1f1a3d;
    --orange: #e9671b;
    --band: #d95a12;
    --white: #ffffff;
    --stick-light: #b4562a;
    --stick-dark: #6e2412;
  }
  * { margin: 0; padding: 0; box-sizing: border-box; }
  html, body { width: 1200px; height: 1200px; overflow: hidden; }
  body { background: var(--page-bg); position: relative; font-family: "Oswald", sans-serif; }

  .pouch-front {
    position: absolute; left: 262px; top: 40px; width: 688px; height: 1130px;
    background: radial-gradient(ellipse at 50% 40%, var(--kraft) 60%, var(--kraft-dark) 100%);
    border-radius: 6px;
  }
  .seal-line {
    position: absolute; left: 36px; right: 36px; top: 92px; height: 6px;
    border-top: 2px solid rgba(0,0,0,0.08); border-bottom: 2px solid rgba(255,255,255,0.12);
  }
  .category {
    position: absolute; top: 172px; width: 100%; text-align: center;
    font-weight: 600; font-size: 29px; color: var(--purple); letter-spacing: 0.5px;
  }
  .brand {
    position: absolute; top: 232px; width: 100%;
    display: flex; align-items: center; justify-content: center; gap: 18px;
  }
  .brand-dot { width: 70px; height: 70px; border-radius: 50%; background: var(--orange); }
  .brand-name { font-weight: 600; font-size: 44px; color: var(--purple); }

  .product-title {
    position: absolute; top: 345px; width: 100%; text-align: center;
    font-family: "Luckiest Guy", sans-serif; color: var(--orange);
    font-size: 118px; line-height: 110px;
    -webkit-text-stroke: 14px var(--white); paint-order: stroke fill;
    transform: rotate(-2deg);
  }

  .product-window { position: absolute; left: 120px; top: 586px; width: 455px; height: 262px; }

  .claim {
    position: absolute; top: 860px; width: 100%; text-align: center;
    font-weight: 700; font-size: 33px; color: var(--navy); z-index: 2;
  }
  .benefit-band {
    position: absolute; left: 69px; width: 559px; top: 877px; height: 127px; background: var(--band);
  }
  .tagline {
    position: absolute; top: 36px; width: 100%; text-align: center;
    font-weight: 600; font-size: 21px; color: var(--white); letter-spacing: 0.3px;
  }
  .badges {
    position: absolute; top: 68px; width: 100%;
    display: flex; justify-content: center; gap: 26px;
  }
  .badge {
    width: 50px; height: 50px; border-radius: 50%; border: 2px solid var(--white);
    display: flex; align-items: center; justify-content: center; text-align: center;
    color: var(--white); font-weight: 500; font-size: 10px; line-height: 11px;
  }
  .net-label {
    position: absolute; top: 1012px; width: 100%; text-align: center;
    font-weight: 600; font-size: 20px; color: var(--navy);
  }
  .net-weight {
    position: absolute; top: 1036px; width: 100%; text-align: center;
    font-weight: 700; font-size: 38px; color: var(--navy); letter-spacing: 0.5px;
  }
</style>
</head>
<body>
  <div class="pouch-front">
    <div class="seal-line"></div>
    <p class="category">COMPLEMENTARY PET FOOD FOR DOGS</p>
    <div class="brand">
      <span class="brand-dot"></span>
      <span class="brand-name">Brisk Nibbles</span>
    </div>
    <h1 class="product-title">BEEF<br>STICKS</h1>

    <svg class="product-window" viewBox="-10 -10 460 265" role="img" aria-label="Bone-shaped clear window showing the beef sticks inside the pouch">
      <defs>
        <linearGradient id="sticks" x1="0" y1="0" x2="1" y2="0">
          <stop offset="0" stop-color="var(--stick-dark)"/>
          <stop offset="0.25" stop-color="var(--stick-light)"/>
          <stop offset="0.5" stop-color="var(--stick-dark)"/>
          <stop offset="0.75" stop-color="var(--stick-light)"/>
          <stop offset="1" stop-color="var(--stick-dark)"/>
        </linearGradient>
      </defs>
      <path d="M105 50 L335 50 A55 55 0 1 1 390 122 A55 55 0 1 1 335 195 L105 195 A55 55 0 1 1 50 122 A55 55 0 1 1 105 50 Z"
            fill="url(#sticks)" stroke="var(--orange)" stroke-width="14" stroke-linejoin="round"/>
    </svg>

    <p class="claim">NATURAL DOG TREATS</p>
    <div class="benefit-band">
      <p class="tagline">HEALTY AND DELICIOUS</p>
      <div class="badges">
        <div class="badge">TASTY<br>BEEF</div>
        <div class="badge">FARM<br>FRESH</div>
        <div class="badge">GLUTEN<br>FREE</div>
      </div>
    </div>
    <p class="net-label">NET WEIGHT</p>
    <p class="net-weight">4 OZ OF GOODNESS</p>
  </div>
</body>
</html>
```